Introduction Post card

Harbourline Doors
27 Varnel Road
Ruthven Ontario
Gus@harbourlinedoorsco.net
519-555-0143

Dear Leamington Residents

We are excited to announce the launch of Harbourline Doors, your new local source for high-quality windows, doors, and garage doors! As a dedicated member of this community, we are committed to providing exceptional products and services that enhance the beauty and functionality of your home or business.

At Harbourline Doors, we understand that choosing the right windows and doors is essential for energy efficiency, security, and style. That’s why we offer a wide selection of premium products tailored to meet your unique needs. Our expert team is here to guide you through the selection process, ensuring you find the perfect fit for your space.

Our services don’t stop at providing quality products. We pride ourselves on our professional installation process, ensuring that every project is completed with precision and care. Customer satisfaction is our top priority, and we strive to exceed your expectations with every interaction.

We invite you to visit our showroom or contact us to learn more about our offerings. Whether you’re looking to upgrade your home’s curb appeal or enhance its security, we are here to help. Together, let’s make our community a more beautiful place!

Thank you for considering Harbourline Doors for your window, door, and garage door needs. We look forward to serving you!

Warm regards,

Gus
Sales Manager
Harbourline Doors
https://harbourlinedoorsco.net/

```html
<!DOCTYPE html>
<html lang="en">
<head>
<meta charset="utf-8">
<title>Harbourline Doors – Introduction Postcard</title>
<link rel="stylesheet" href="https://fonts.googleapis.com/css2?family=Montserrat:ital,wght@0,400;0,500;0,600;1,600&family=Rubik:wght@900&display=swap">
<style>
  :root {
    --orange: #e8602c;
    --charcoal: #3d3c39;
    --white: #ffffff;
    --paper: #fafafa;
    --stage: #e4e7ea;
    --rule: #8a8a8a;
    --photo-tone: #b9c6d2;
  }
  * { box-sizing: border-box; margin: 0; padding: 0; }
  html, body { width: 1200px; height: 1192px; overflow: hidden; }
  body {
    background: var(--stage);
    font-family: "Montserrat", Arial, sans-serif;
    position: relative;
  }
  .postcard {
    position: absolute;
    left: 210px;
    width: 780px;
    height: 558px;
    overflow: hidden;
    box-shadow: 0 6px 18px rgba(0,0,0,.18);
  }
  .postcard--front { top: 26px; }
  .postcard--back { top: 608px; background: var(--paper); }

  /* Front */
  .hero-photo {
    position: absolute; inset: 0;
    background: var(--photo-tone);
  }
  .brand {
    position: absolute; top: 28px; left: 258px;
    display: flex; align-items: center; gap: 14px;
  }
  .brand__mark { width: 22px; height: 22px; background: var(--charcoal); }
  .brand__name {
    font-weight: 600; color: var(--orange);
    font-size: 30px; line-height: 1; letter-spacing: .5px;
  }
  .front-band { position: absolute; left: 0; top: 0; width: 780px; height: 558px; }
  .welcome {
    position: absolute; left: 27px; top: 382px; color: var(--white);
  }
  .welcome__lead {
    font-style: italic; font-weight: 600; color: var(--charcoal);
    font-size: 28px; letter-spacing: -1.5px; line-height: 1;
  }
  .welcome__title {
    font-family: "Rubik", Arial, sans-serif; font-weight: 900;
    font-size: 39px; line-height: .95; margin-top: 5px; letter-spacing: .5px;
  }
  .welcome__tag { font-size: 12.5px; line-height: 1.35; margin-top: 12px; width: 360px; }
  .contact {
    position: absolute; left: 514px; top: 456px; color: var(--white);
    list-style: none; font-size: 13.5px; line-height: 18px;
  }
  .contact li { display: flex; align-items: center; gap: 8px; }
  .contact svg { width: 11px; height: 11px; flex: none; fill: var(--white); }
  .contact svg.icon-line { fill: none; stroke: var(--white); stroke-width: 2.4; }
  .contact .contact__phone {
    font-family: "Rubik", Arial, sans-serif; font-weight: 900;
    font-size: 24px; line-height: 28px; letter-spacing: .5px;
  }

  /* Back */
  .letter {
    position: absolute; left: 0; top: 0; width: 440px; height: 466px;
    background: var(--charcoal); color: var(--white);
    padding: 20px 16px 0 28px; font-size: 12.2px; line-height: 14.2px;
  }
  .letter__greeting { font-size: 13.5px; line-height: 16px; margin-bottom: 6px; }
  .letter p { margin-bottom: 14.2px; }
  .signoff {
    position: absolute; left: 0; top: 474px; width: 440px; height: 84px;
    background: var(--orange); color: var(--white);
    font-size: 13px; line-height: 14px; padding: 12px 28px;
  }
  .signoff__web { position: absolute; right: 24px; bottom: 15px; font-size: 14px; }
  .address-side { position: absolute; left: 440px; top: 0; width: 340px; height: 558px; background: var(--paper); }
  .stamp-box {
    position: absolute; right: 18px; top: 28px; width: 96px; height: 122px;
    border: 1px solid var(--rule);
  }
  .address-line {
    position: absolute; left: 32px; right: 18px; height: 1px; background: var(--rule);
  }
</style>
</head>
<body>

<section class="postcard postcard--front" aria-label="Postcard front">
  <div class="hero-photo" role="img" aria-label="Photo placeholder: modern two-storey house with lawn under a cloudy sky"></div>

  <div class="brand">
    <span class="brand__mark"></span>
    <span class="brand__name">HARBOURLINE<br>DOORS</span>
  </div>

  <svg class="front-band" viewBox="0 0 780 558" aria-hidden="true">
    <polygon points="0,355 318,355 382,420 780,420 780,436 378,436 312,371 0,371" fill="var(--charcoal)"/>
    <polygon points="0,371 312,371 378,436 780,436 780,440 376,440 310,375 0,375" fill="var(--white)"/>
    <polygon points="0,375 310,375 376,440 780,440 780,558 0,558" fill="var(--orange)"/>
  </svg>

  <div class="welcome">
    <div class="welcome__lead">Welcome to</div>
    <div class="welcome__title">HARBOURLINE<br>DOORS!</div>
    <div class="welcome__tag">Your Local Experts in High-Quality Windows, Doors,<br>and Garage Doors!</div>
  </div>

  <ul class="contact">
    <li class="contact__phone">
      <svg viewBox="0 0 24 24"><path d="M6.6 10.8a15.1 15.1 0 0 0 6.6 6.6l2.2-2.2c.3-.3.7-.4 1-.2 1.1.4 2.3.6 3.6.6.6 0 1 .4 1 1V20c0 .6-.4 1-1 1A17 17 0 0 1 3 4c0-.6.4-1 1-1h3.5c.6 0 1 .4 1 1 0 1.3.2 2.5.6 3.6.1.3 0 .7-.2 1z"/></svg>
      519-555-0143
    </li>
    <li>
      <svg class="icon-line" viewBox="0 0 24 24"><path d="M2 5h20v14H2z M2 5l10 8 10-8"/></svg>
      Gus@harbourlinedoorsco.net
    </li>
    <li>
      <svg class="icon-line" viewBox="0 0 24 24"><circle cx="12" cy="12" r="9.5"/><path d="M2.5 12h19M12 2.5c3 3 3 16 0 19M12 2.5c-3 3-3 16 0 19"/></svg>
      www.harbourlinedoorsco.net
    </li>
    <li>
      <svg viewBox="0 0 24 24"><path d="M12 2a7 7 0 0 0-7 7c0 5 7 13 7 13s7-8 7-13a7 7 0 0 0-7-7zm0 9.5A2.5 2.5 0 1 1 12 6.5a2.5 2.5 0 0 1 0 5z"/></svg>
      27 Varnel Road, Ruthven, Ontario
    </li>
  </ul>
</section>

<section class="postcard postcard--back" aria-label="Postcard back">
  <article class="letter">
    <div class="letter__greeting">Dear Leamington Residents</div>
    <p>We are excited to announce the launch of Harbourline Doors, your new local source for high-quality windows, doors, and garage doors! As a dedicated member of this community, we are committed to providing exceptional products and services that enhance the beauty and functionality of your home or business.</p>
    <p>At Harbourline Doors, we understand that choosing the right windows and doors is essential for energy efficiency, security, and style. That’s why we offer a wide selection of premium products tailored to meet your unique needs. Our expert team is here to guide you through the selection process, ensuring you find the perfect fit for your space.</p>
    <p>Our services don’t stop at providing quality products. We pride ourselves on our professional installation process, ensuring that every project is completed with precision and care. Customer satisfaction is our top priority, and we strive to exceed your expectations with every interaction.</p>
    <p>We invite you to visit our showroom or contact us to learn more about our offerings. Whether you’re looking to upgrade your home’s curb appeal or enhance its security, we are here to help. Together, let’s make our community a more beautiful place!</p>
    <p>Thank you for considering Harbourline Doors for your window, door, and garage door needs. We look forward to serving you!</p>
    <p>Warm regards,</p>
  </article>

  <footer class="signoff">
    Gus<br>Sales Manager<br>Harbourline Doors
    <span class="signoff__web">www.harbourlinedoorsco.net</span>
  </footer>

  <div class="address-side">
    <div class="stamp-box"></div>
    <div class="address-line" style="top:332px"></div>
    <div class="address-line" style="top:383px"></div>
    <div class="address-line" style="top:434px"></div>
    <div class="address-line" style="top:485px"></div>
  </div>
</section>

</body>
</html>
```